Pest control srevice Special offer

Pest control to promote our service program. 3 month pest control service for $125.00 Includes svc for ants,bees,wasps,silverfish,rats,mice,roaches. No long term contracts Our customers can purchase the service 3 months at a time as needed throughout the year. Or sign up for the full year at 425.00

Target Market(s)

Home Owners

Industry/Entity Type

Pest Control

Font styles to use
Sans Serif

Requirements
Must have
• must be relevant to pest control see our web site at brindlecovepestcontrol.example
Nice to have
• I want the post card to be laid out in a way that describes our service simple and professional. The program that we are offering really works well for our customers and makes sense they only pay for service when they are having an issue
Should not have
• I don't want pictures of insects that scare people off or unsettling to look at

```html
<!DOCTYPE html>
<html lang="en">
<head>
<meta charset="utf-8">
<title>Brindle Cove Pest Control – 3 Month Service Postcard</title>
<link rel="stylesheet" href="https://fonts.googleapis.com/css2?family=Oswald:wght@500;600;700&family=Roboto+Condensed:wght@700&display=swap">
<style>
  :root {
    --backdrop: #2a2a2a;
    --card: #ffffff;
    --header-veil: rgba(255,255,255,0.86);
    --ink: #111111;
    --red: #e0262a;
    --yellow: #fdd32b;
    --green: #4a9a1f;
    --brown: #4a2410;
    --white: #ffffff;
    --leaf-dark: #2f3d22;
    --leaf-mid: #5f7d3e;
    --leaf-light: #a7b98a;
  }
  * { margin: 0; padding: 0; box-sizing: border-box; }
  html, body { width: 1200px; height: 933px; overflow: hidden; }
  body { background: var(--backdrop); position: relative; font-family: "Oswald", sans-serif; }

  .postcard {
    position: absolute; left: 67px; top: 67px;
    width: 1067px; height: 800px;
    background: var(--card); overflow: hidden;
  }

  .service-photo {
    position: absolute; left: 0; top: 0; width: 1067px; height: 527px;
    background:
      radial-gradient(ellipse at 88% 55%, var(--leaf-mid) 0%, rgba(95,125,62,0) 45%),
      radial-gradient(ellipse at 12% 45%, #d9d6cf 0%, rgba(217,214,207,0) 22%),
      linear-gradient(100deg, var(--leaf-light) 0%, var(--leaf-dark) 45%, #3f5a2c 70%, var(--leaf-mid) 100%);
  }

  .header-strip {
    position: absolute; left: 0; top: 0; width: 1067px; height: 112px;
    background: var(--header-veil);
  }
  .brand {
    position: absolute; left: 18px; top: 20px; width: 160px;
    font-family: "Oswald", sans-serif; font-weight: 600;
    font-size: 22px; line-height: 1.05; color: var(--ink);
    text-align: center; text-transform: uppercase;
  }
  .estimate {
    position: absolute; right: 14px; top: 16px; text-align: right;
  }
  .estimate-label {
    font-weight: 600; font-size: 25px; color: var(--ink); line-height: 1.1;
  }
  .estimate-phone {
    font-weight: 700; font-size: 47px; color: var(--red); line-height: 1.05;
  }

  .offer-band { position: absolute; left: 0; top: 463px; width: 1067px; height: 152px; }
  .offer-band svg { position: absolute; left: 0; top: 0; }
  .pests {
    position: absolute; left: 28px; top: 16px; width: 500px;
    font-family: "Oswald", sans-serif; font-weight: 600; color: var(--ink);
    text-transform: uppercase; white-space: nowrap;
  }
  .pests-heading { font-size: 32px; line-height: 1.2; }
  .pests-list { font-size: 28px; line-height: 1.2; margin-top: 4px; }
  .price {
    position: absolute; left: 582px; top: 16px;
    color: var(--white); font-weight: 600; font-size: 104px; line-height: 1;
    white-space: nowrap;
  }
  .price sup { font-size: 48px; position: relative; top: -38px; vertical-align: baseline; }
  .price-divider {
    position: absolute; left: 780px; top: 22px; width: 2px; height: 108px;
    background: rgba(120,10,10,0.75);
  }
  .term { position: absolute; left: 800px; top: 24px; text-transform: uppercase; white-space: nowrap; }
  .term-length { color: var(--yellow); font-weight: 700; font-size: 52px; line-height: 1.05; letter-spacing: 0.5px; }
  .term-label {
    color: var(--white); font-family: "Roboto Condensed", sans-serif; font-weight: 700;
    font-size: 23px; line-height: 1.3; margin-top: 6px;
  }

  .terms-band {
    position: absolute; left: 0; top: 616px; width: 1067px; height: 120px;
    background: var(--green); color: var(--white);
    font-family: "Roboto Condensed", sans-serif; font-weight: 700;
    font-size: 23px; line-height: 42px; text-align: center; text-transform: uppercase;
    padding-top: 18px;
  }

  .contact-band {
    position: absolute; left: 0; top: 736px; width: 1067px; height: 64px;
    background: var(--brown); color: var(--white);
    font-family: "Roboto Condensed", sans-serif; font-weight: 700;
    font-size: 21px; line-height: 64px; text-align: center;
  }
</style>
</head>
<body>
  <article class="postcard">
    <div class="service-photo" role="img" aria-label="Technician in gloves spraying shrubs in a garden with a hose wand"></div>

    <header class="header-strip">
      <div class="brand">Brindle Cove Pest Control</div>
      <div class="estimate">
        <p class="estimate-label">CALL FOR A FREE ESTIMATE!</p>
        <p class="estimate-phone">800-555-0147</p>
      </div>
    </header>

    <section class="offer-band">
      <svg width="1067" height="152" viewBox="0 0 1067 152" aria-hidden="true">
        <rect x="520" y="0" width="547" height="152" fill="var(--red)"/>
        <polygon points="0,0 522,0 562,76 522,152 0,152" fill="var(--yellow)"/>
        <polyline points="536,-2 577,76 536,154" fill="none" stroke="var(--white)" stroke-width="6"/>
      </svg>
      <div class="pests">
        <p class="pests-heading">Includes svc for</p>
        <p class="pests-list">Ants,bees,wasps,silverfish, rats<br>mice,roaches</p>
      </div>
      <p class="price"><sup>$</sup>125</p>
      <div class="price-divider"></div>
      <div class="term">
        <p class="term-length">3 Months</p>
        <p class="term-label">Pest Control Service</p>
      </div>
    </section>

    <section class="terms-band">
      No long term contracts our customers can purchase the service 3 months at<br>
      a time as needed throughout the year. Or sign up for the full year at 425.00
    </section>

    <footer class="contact-band">
      18 Alder Court Pittsburgh, PA 15209 &nbsp;• Our Website : www.brindlecovepestcontrol.example
    </footer>
  </article>
</body>
</html>
```